Crowdsourced IT recruitment agency - brivon

We need an engaging and smart website design for BRIVON Crowd recruitment. We are young innovative IT recruitment company. We have deep expertise in all IT & digital areas and using crowdsourcing to search the best market candidates faster than ever.
Our mission: to connect people and organizations interests, inspiring each other and enabling together reach better results.

We would like the design to be personalized, emotional, yet simple and neat. It should focus on the person with a problem which we solve.

Reading the site customers should feel safe and confident that brivon is the trusted partner and everything we do is a quality product.

We also focus on long term relationship with our clients.

We have 4 products:
IT Recruitment – professional recruitment of candidates in IT and digital areas
IT RPO – candidates research process outsourcing(RPO) - provision of resume pools for the client
Velmar Academy – training, seminars and networking events for HR professionals from IT and hi-tech companies
HR Dashboard – a tool for data visualization in nice and interactive dashboards. It pulls data from different corporate sources (SAP, Oracle, excel, etc.). It looks like a dashboard, on which there are several graphs or diagrams with HR and business KPIs(key performance indicators)

We like material design sites but also open for other options/ideas

Current site brivon.ru

Examples of websites that we like:
http://www.kelmo.ru
https://pinegroverun.ru

Site structure:
About us (description, mission, team, clients, office)
Products: HR Dashboard, HR IPO, It Recruitment
Velmar Academy (list of events (past and future) with the ability to upload photos, descriptions, etc.)
News: Publications, Articles, Blog
Contacts

Industry/Entity Type

Consulting

Number of Pages Required

5+ page

Font styles to use
Serif
Sans Serif

Requirements
Must have
• Individual blocks with the transition to a separate page for each product
• Link to social network (fb, link),
• Subscribe to news on the main page
• Feedback form
• Site structure:
• About us (description, mission, team, clients, office)
• Products: HR Dashboard, HR IPO, It Recruitment
• Velmar Academy (list of events (past and future) with the ability to upload photos, descriptions, etc.)
• News: Publications, Articles, Blog, Calendars
• Contacts
Should not have
• too crowded
• too complicatied
• without advertising banners
• crammed

```html
<!DOCTYPE html>
<html lang="en">
<head>
<meta charset="utf-8">
<title>Brivon — Crowd Recruitment</title>
<link href="https://fonts.googleapis.com/css2?family=Roboto+Condensed:wght@400;700&family=Roboto:ital,wght@0,400;0,500;0,700;1,400&display=swap" rel="stylesheet">
<style>
:root{
  --blue:#2f5d9f;
  --blue-dark:#25497f;
  --green:#4b7a3b;
  --ink:#222;
  --text:#555;
  --muted:#888;
  --cream:#fbf6ec;
  --cream-line:#efe3cc;
  --footer:#f4f4f4;
  --white:#fff;
}
*{box-sizing:border-box;margin:0;padding:0}
html,body{width:1200px;height:3364px;overflow:hidden;background:var(--white)}
body{position:relative;font-family:"Roboto",Arial,sans-serif;color:var(--text);font-size:11px;line-height:1.55}
.abs{position:absolute}
.heading{font-family:"Roboto Condensed","Arial Narrow",sans-serif;color:var(--ink);font-weight:400}

/* header */
.site-header{left:0;top:0;width:1200px;height:124px;background:var(--white)}
.brand{display:flex;align-items:center;gap:12px}
.brand-mark{width:58px;height:58px;border-radius:50%;background:var(--blue)}
.brand-name{font-family:"Roboto",sans-serif;font-weight:700;font-size:30px;color:var(--blue);line-height:1}
.brand-sub{font-size:11px;color:var(--ink);letter-spacing:.5px;margin-top:2px}
.contact-top{top:28px;display:flex;align-items:center;gap:10px;font-size:13px;color:#444}
.dot-icon{width:24px;height:24px;border-radius:50%;background:var(--blue);display:flex;align-items:center;justify-content:center}
.main-nav{top:80px;right:96px;display:flex;gap:0;font-size:12px;color:#333}
.main-nav a{padding:0 13px;height:24px;line-height:24px;color:#333;text-decoration:none}
.main-nav a.active{background:#e8eef7;border-radius:50%;color:var(--blue);padding:0 8px}

/* hero */
.hero{left:0;top:124px;width:1200px;height:542px;background:linear-gradient(90deg,#5a5560 0%,#8b8489 45%,#b9b4b2 75%,#9a9797 100%)}
.hero-title{left:99px;top:322px;font-family:"Roboto Condensed",sans-serif;font-size:40px;line-height:42px;color:var(--white);font-weight:400}
.hero-sub{left:99px;top:414px;width:340px;font-size:13px;color:var(--white)}
.hero-dots{left:99px;top:472px;display:flex;gap:8px}
.hero-dots span{width:12px;height:12px;border-radius:50%;background:var(--white)}
.hero-dots span.on{box-shadow:0 0 0 3px rgba(255,255,255,.5)}

/* about */
.about{left:0;top:666px;width:1200px;height:426px}
.about-title{left:99px;top:766px;font-size:30px}
.about-title em{font-style:normal;color:var(--blue)}
.about-text{left:99px;width:390px;font-size:10.5px;color:#666}
.btn{display:inline-block;background:var(--blue);color:var(--white);font-size:11px;text-transform:uppercase;letter-spacing:.3px;text-align:center;text-decoration:none}
.panel-title{font-family:"Roboto Condensed",sans-serif;font-size:26px;color:var(--white)}
.panel-text{width:360px;font-size:10.5px;color:#e6edf6}
.panel-link{font-size:10px;color:var(--white);font-weight:700}

/* products */
.section-title{width:1200px;left:0;text-align:center;font-size:33px}
.section-sub{width:1200px;left:0;text-align:center;font-size:11px;color:#666}
.product-card{top:1263px;width:236px;height:289px;text-align:center}
.product-card svg.frame{position:absolute;left:0;top:0}
.product-icon{position:absolute;left:73px;top:29px;width:90px;height:90px;border-radius:50%;background:var(--blue);display:flex;align-items:center;justify-content:center}
.product-name{position:absolute;left:0;top:142px;width:236px;font-size:13px;color:#333;text-transform:uppercase}
.product-desc{position:absolute;left:28px;top:170px;width:180px;font-size:10.5px;color:#666;line-height:1.6}
.product-link{position:absolute;left:58px;top:260px;width:120px;font-size:10px;color:var(--blue);text-transform:uppercase;border-top:1px solid #cfd8e6;padding-top:6px}

/* academy */
.academy{left:0;top:1649px;width:1200px;height:471px;background:linear-gradient(90deg,#fafafa 0%,#f0f1f2 55%,#e4e6e8 100%)}
.academy-photo{left:700px;top:1649px;width:500px;height:471px;background:linear-gradient(120deg,rgba(240,242,244,0) 0%,#c9d5e2 25%,#6d95c6 55%,#8aa9cf 80%,#cfd6dd 100%)}
.academy-title{left:99px;top:1750px;font-size:34px;color:#222}
.academy-text{left:99px;width:520px;font-size:10.5px;color:#555}

/* blog */
.blog-card{top:2272px;width:309px}
.blog-image{width:309px;height:157px}
.blog-title{margin-top:18px;text-align:center;font-size:17px;color:#333}
.blog-meta{text-align:center;font-size:10.5px;font-style:italic;color:#333;margin-top:6px}
.blog-meta span{margin:0 10px;color:#999}
.blog-meta em{color:var(--blue)}
.blog-excerpt{text-align:center;font-size:10.5px;color:#666;margin-top:6px;padding:0 40px;line-height:1.5}
.pager{top:2575px;left:572px;display:flex;gap:6px}
.pager span{width:22px;height:22px;border:1px solid #bbb;border-radius:50%;display:flex;align-items:center;justify-content:center}

/* testimonials */
.testimonials{left:0;top:2665px;width:1200px;height:341px;background:linear-gradient(160deg,#4d78b6 0%,#3f6aab 60%,#3a65a4 100%)}
.testi-title{left:0;top:2728px;width:1200px;text-align:center;font-family:"Roboto Condensed",sans-serif;font-size:30px;color:var(--white)}
.testi-quote{left:205px;top:2790px;width:800px;text-align:center;font-size:11px;color:#eef2f8;line-height:1.55}
.testi-name{left:0;top:2878px;width:1200px;text-align:center;font-size:17px;font-style:italic;color:var(--white)}
.testi-name small{font-size:11px}
.testi-dots{left:551px;top:2925px;display:flex;gap:6px}
.testi-dots span{width:30px;height:3px;background:rgba(255,255,255,.45)}
.testi-dots span.on{background:var(--white)}

/* footer */
.site-footer{left:0;top:3006px;width:1200px;height:309px;background:var(--footer)}
.footer-heading{font-family:"Roboto Condensed",sans-serif;font-size:16px;color:#333;text-transform:uppercase;letter-spacing:.3px}
.footer-text{font-size:10.5px;color:#555;line-height:1.6}
.social{display:flex;gap:6px}
.social span{width:22px;height:22px;border:1px solid #555;border-radius:50%}
.field{width:305px;height:40px;background:var(--white);border:1px solid #ddd;font-size:10.5px;color:#888;padding:12px}
.contact-row{display:flex;gap:14px;font-size:11px;color:#555;line-height:1.6}
.quick-links{list-style:none;font-size:10.5px;color:#555;line-height:22.4px}
.quick-links li::before{content:"";display:inline-block;border-left:4px solid #555;border-top:3px solid transparent;border-bottom:3px solid transparent;margin-right:10px}
.copyright{left:0;top:3315px;width:1200px;height:49px;background:var(--white);text-align:center;line-height:49px;font-size:10px;color:#555}
</style>
</head>
<body>

<header class="abs site-header">
  <div class="abs brand" style="left:99px;top:18px">
    <div class="brand-mark"></div>
    <div>
      <div class="brand-name">brivon</div>
      <div class="brand-sub">CROWD RECRUITMENT</div>
    </div>
  </div>
  <div class="abs contact-top" style="left:790px">
    <span class="dot-icon"><svg width="12" height="12" viewBox="0 0 24 24"><path fill="#fff" d="M6.6 10.8a15 15 0 0 0 6.6 6.6l2.2-2.2a1 1 0 0 1 1-.25 11.4 11.4 0 0 0 3.6.57 1 1 0 0 1 1 1V20a1 1 0 0 1-1 1A17 17 0 0 1 3 4a1 1 0 0 1 1-1h3.5a1 1 0 0 1 1 1c0 1.25.2 2.45.57 3.57a1 1 0 0 1-.25 1z"/></svg></span>
    <span>(902) 555-0147</span>
  </div>
  <div class="abs contact-top" style="left:952px">
    <span class="dot-icon"><svg width="12" height="10" viewBox="0 0 24 18"><rect x="1" y="1" width="22" height="16" rx="2" fill="#fff"/><path d="M2 2l10 8 10-8" stroke="#2f5d9f" stroke-width="2" fill="none"/></svg></span>
    <span>info@brivon.ru</span>
  </div>
  <nav class="abs main-nav">
    <a class="active" href="#">HOME</a><a href="#">ABOUT US</a><a href="#">OUR PRODUCTS</a><a href="#">VELMAR ACADEMY</a><a href="#">NEWS</a><a href="#">CONTACT US</a>
  </nav>
</header>

<section class="abs hero" role="img" aria-label="Photo of two smiling businesswomen in a bright modern office lounge with purple sofas"></section>
<h1 class="abs hero-title">BRIVON<br>CROWD RECRUITMENT</h1>
<p class="abs hero-sub">Sed ut perspiciatis unde omnis iste natus error sit voluptatem accusantium doloremque</p>
<div class="abs hero-dots"><span class="on"></span><span></span><span></span><span></span></div>

<section class="abs about">
  <svg class="abs" style="left:0;top:0" width="1200" height="426" viewBox="0 0 1200 426">
    <polygon points="498,0 1200,0 1200,213 561,213" fill="#2f5d9f"/>
    <polygon points="561,213 1200,213 1200,426 498,426" fill="#4b7a3b"/>
    <circle cx="220" cy="180" r="150" fill="#f3f6fa"/>
  </svg>
</section>
<h2 class="abs heading about-title">WELCOME TO <em>BRIVON</em></h2>
<p class="abs about-text" style="top:816px">Sed ut perspiciatis unde omnis iste natus error sit voluptatem accusantium doloremque laudantium, totam rem aperiam, eaque ipsa quae ab illo inventore veritatis et quasi architecto beatae vitae dicta sunt explicabo. Nemo enim ipsam voluptatem</p>
<p class="abs about-text" style="top:904px">Sed ut perspiciatis unde omnis iste natus error sit voluptatem accusantium doloremque laudantium, totam rem aperiam.</p>
<a class="abs btn" style="left:99px;top:969px;width:96px;height:29px;line-height:29px">Read more</a>

<svg class="abs" style="left:622px;top:710px" width="44" height="44" viewBox="0 0 44 44"><circle cx="22" cy="22" r="19" fill="none" stroke="#fff" stroke-width="3"/><circle cx="22" cy="22" r="12" fill="none" stroke="#fff" stroke-width="3"/><circle cx="22" cy="22" r="5" fill="#fff"/></svg>
<div class="abs panel-title" style="left:686px;top:706px">OUR MISSION</div>
<p class="abs panel-text" style="left:690px;top:752px">Sed ut perspiciatis unde omnis iste natus error sit voluptatem accusantium doloremque laudantium, totam rem aperiam, eaque ipsa quae ab illo inventore veritatis et quasi architecto beatae vitae dicta sunt.</p>
<div class="abs panel-link" style="left:690px;top:826px">READ MORE &#9679;</div>

<svg class="abs" style="left:620px;top:918px" width="50" height="40" viewBox="0 0 50 40"><circle cx="25" cy="10" r="8" fill="#fff"/><path d="M11 38c0-10 6-16 14-16s14 6 14 16z" fill="#fff"/><circle cx="9" cy="15" r="6" fill="#fff"/><path d="M0 34c0-7 4-11 9-11 2 0 3 .5 4 1-2 3-3 6-3 10z" fill="#fff"/><circle cx="41" cy="15" r="6" fill="#fff"/><path d="M50 34c0-7-4-11-9-11-2 0-3 .5-4 1 2 3 3 6 3 10z" fill="#fff"/></svg>
<div class="abs panel-title" style="left:686px;top:914px">OUR TEAM</div>
<p class="abs panel-text" style="left:690px;top:960px">Sed ut perspiciatis unde omnis iste natus error sit voluptatem accusantium doloremque laudantium, totam rem aperiam, eaque ipsa quae ab illo inventore veritatis et quasi architecto beatae vitae dicta sunt.</p>
<div class="abs panel-link" style="left:690px;top:1036px">READ MORE &#9679;</div>

<div class="abs" style="left:0;top:1092px;width:1200px;height:1px;background:#e6e6e6"></div>
<h2 class="abs heading section-title" style="top:1164px">OUR PRODUCTS</h2>
<p class="abs section-sub" style="top:1212px">Sed ut perspiciatis unde omnis iste natus error sit voluptatem</p>

<article class="abs product-card" style="left:105px">
  <svg class="frame" width="236" height="289" viewBox="0 0 236 289"><polygon points="1,1 118,14 235,1 235,288 1,288" fill="#fbf6ec" stroke="#efe3cc"/></svg>
  <div class="product-icon"><svg width="40" height="34" viewBox="0 0 40 34"><rect x="2" y="2" width="30" height="20" rx="1" fill="none" stroke="#fff" stroke-width="2.5"/><path d="M12 28h10M17 22v6" stroke="#fff" stroke-width="2.5"/><circle cx="33" cy="26" r="6" fill="none" stroke="#fff" stroke-width="2.5"/></svg></div>
  <h3 class="product-name">IT Recruitment</h3>
  <p class="product-desc">professional recruitment of candidates in IT and digital areas Sed ut perspiciatis unde omnis</p>
  <div class="product-link">Read more info</div>
</article>
<article class="abs product-card" style="left:357px">
  <svg class="frame" width="236" height="289" viewBox="0 0 236 289"><polygon points="1,1 118,14 235,1 235,288 1,288" fill="#fbf6ec" stroke="#efe3cc"/></svg>
  <div class="product-icon"><svg width="42" height="30" viewBox="0 0 42 30"><rect x="7" y="2" width="28" height="19" rx="1" fill="none" stroke="#fff" stroke-width="2.5"/><path d="M2 26h38" stroke="#fff" stroke-width="3.5" stroke-linecap="round"/></svg></div>
  <h3 class="product-name">IT RPO</h3>
  <p class="product-desc">candidates research process outsourcing(RPO) - provision of resume pools for the client</p>
  <div class="product-link">Read more info</div>
</article>
<article class="abs product-card" style="left:608px">
  <svg class="frame" width="236" height="289" viewBox="0 0 236 289"><polygon points="1,1 118,14 235,1 235,288 1,288" fill="#fbf6ec" stroke="#efe3cc"/></svg>
  <div class="product-icon"><svg width="44" height="32" viewBox="0 0 44 32"><polygon points="22,2 42,11 22,20 2,11" fill="#fff"/><path d="M11 16v8c0 3 5 5 11 5s11-2 11-5v-8l-11 5z" fill="#fff"/><path d="M39 12v10" stroke="#fff" stroke-width="2"/></svg></div>
  <h3 class="product-name">Velmar Academy</h3>
  <p class="product-desc">training, seminars and networking events for HR professionals from IT and hi-tech companies</p>
  <div class="product-link">Read more info</div>
</article>
<article class="abs product-card" style="left:857px">
  <svg class="frame" width="236" height="289" viewBox="0 0 236 289"><polygon points="1,1 118,14 235,1 235,288 1,288" fill="#fbf6ec" stroke="#efe3cc"/></svg>
  <div class="product-icon"><svg width="34" height="38" viewBox="0 0 34 38"><path d="M3 2h20l8 8v26H3z" fill="none" stroke="#fff" stroke-width="2.5"/><path d="M9 14h16M9 20h16M9 26h10" stroke="#fff" stroke-width="2.2"/></svg></div>
  <h3 class="product-name">HR Dashboard</h3>
  <p class="product-desc">a tool for data visualization in nice and interactive dashboards. It pulls data from different corporate</p>
  <div class="product-link">Read more info</div>
</article>

<section class="abs academy"></section>
<div class="abs academy-photo" role="img" aria-label="Photo of a smiling man and woman working together at a laptop in a bright office"></div>
<h2 class="abs heading academy-title">VELMAR ACADEMY</h2>
<p class="abs academy-text" style="top:1812px">Sed ut perspiciatis unde omnis iste natus error sit voluptatem accusantium doloremque laudantium, totam rem aperiam, eaque ipsa quae ab illo inventore veritatis et quasi architecto beatae vitae dicta sunt explicabo. Nemo enim ipsam</p>
<p class="abs academy-text" style="top:1890px">Sed ut perspiciatis unde omnis iste natus error sit voluptatem accusantium doloremque laudantium, totam rem aperiam, eaque ipsa quae ab illo inventore veritatis et quasi architecto beatae vitae dicta sunt explicabo. Nemo enim ipsam</p>
<a class="abs btn" style="left:99px;top:1969px;width:113px;height:32px;line-height:32px;font-size:12px">Read more</a>

<h2 class="abs heading section-title" style="top:2189px">LATEST BLOG</h2>
<article class="abs blog-card" style="left:99px">
  <div class="blog-image" role="img" aria-label="Photo of hands arranging colourful sticky notes beside a tablet on a desk" style="background:linear-gradient(135deg,#b56f4f,#3f8a94 55%,#c9a27a)"></div>
  <h3 class="heading blog-title">Sed ut perspiciatis unde</h3>
  <div class="blog-meta">Jan 21, 2017<span>\</span><em>2 comments</em></div>
  <p class="blog-excerpt">Lorem ipsum dolor sit amet, consectetur adipiscing Sed blandit massa vel mauris sollicitudin</p>
</article>
<article class="abs blog-card" style="left:444px">
  <div class="blog-image" role="img" aria-label="Photo of a young man with a phone in a sunny city street" style="background:linear-gradient(120deg,#6f7f8f,#a9a8a0 50%,#e8c27a)"></div>
  <h3 class="heading blog-title">Sed ut perspiciatis unde</h3>
  <div class="blog-meta">Jan 21, 2017<span>\</span><em>2 comments</em></div>
  <p class="blog-excerpt">Lorem ipsum dolor sit amet, consectetur adipiscing Sed blandit massa vel mauris sollicitudin</p>
</article>
<article class="abs blog-card" style="left:792px">
  <div class="blog-image" role="img" aria-label="Photo of a team of colleagues gathered around a laptop in a meeting" style="background:linear-gradient(120deg,#8fa6b8,#4d77a8 50%,#c4cfd8)"></div>
  <h3 class="heading blog-title">Sed ut perspiciatis unde</h3>
  <div class="blog-meta">Jan 21, 2017<span>\</span><em>2 comments</em></div>
  <p class="blog-excerpt">Lorem ipsum dolor sit amet, consectetur adipiscing Sed blandit massa vel mauris sollicitudin</p>
</article>
<div class="abs pager">
  <span><svg width="8" height="8" viewBox="0 0 8 8"><path d="M5 1L2 4l3 3" stroke="#777" fill="none" stroke-width="1.5"/></svg></span>
  <span><svg width="8" height="8" viewBox="0 0 8 8"><path d="M3 1l3 3-3 3" stroke="#777" fill="none" stroke-width="1.5"/></svg></span>
</div>

<section class="abs testimonials"></section>
<h2 class="abs testi-title">TESTIMONIALS</h2>
<p class="abs testi-quote">&ldquo; Lorem ipsum dolor sit amet, consectetur adipiscing elit, sed do eiusmod tempor incididunt ut labore et dolore magna aliqua. Ut enim ad minim veniam, quis nostrud exercitation ullamco laboris nisi ut aliquip ex ea commodo consequat. Duis aute irure dolor in reprehenderit in voluptate velit esse cillum dolore eu fugiat nulla Sed ut perspiciatis unde omnis iste natus error sit voluptatem accusantium doloremque laudantium, totam rem aperiam, eaque ipsa quae ab illo inventore veritatis et quasi architecto beatae vitae</p>
<div class="abs testi-name">Mark Ellison <small>- Brivon</small></div>
<div class="abs testi-dots"><span class="on"></span><span></span><span></span></div>

<footer class="abs site-footer">
  <div class="abs brand" style="left:99px;top:55px">
    <div class="brand-mark" style="width:62px;height:62px"></div>
    <div>
      <div class="brand-name" style="font-size:28px">brivon</div>
      <div class="brand-sub">CROWD RECRUITMENT</div>
    </div>
  </div>
  <p class="abs footer-text" style="left:99px;top:140px;width:230px">Sed ut perspiciatis unde omnis iste natus error sit voluptatem accusantium doloremque laudantium, totam rem aperiam.</p>
  <div class="abs social" style="left:99px;top:220px"><span></span><span></span><span></span><span></span></div>

  <h4 class="abs footer-heading" style="left:406px;top:64px">Sign up for newsletter</h4>
  <p class="abs footer-text" style="left:406px;top:98px;width:240px">Excepteur sint occaecat cupidatat non proident, sunt in culpa qui officia deserunt</p>
  <div class="abs field" style="left:406px;top:146px">Enter email</div>
  <a class="abs btn" style="left:406px;top:200px;width:120px;height:32px;line-height:32px;font-size:10.5px;background:var(--blue-dark)">Subscription</a>

  <h4 class="abs footer-heading" style="left:718px;top:64px">Contact us</h4>
  <div class="abs contact-row" style="left:718px;top:102px"><svg width="12" height="16" viewBox="0 0 12 16"><path d="M6 0a6 6 0 0 0-6 6c0 4.5 6 10 6 10s6-5.5 6-10a6 6 0 0 0-6-6zm0 8.5A2.5 2.5 0 1 1 6 3.5a2.5 2.5 0 0 1 0 5z" fill="#555"/></svg><span>Brivon<br>48 Harlow Lane, Westbury, Nc,<br>27519</span></div>
  <div class="abs contact-row" style="left:718px;top:176px"><svg width="13" height="13" viewBox="0 0 24 24"><path fill="#555" d="M6.6 10.8a15 15 0 0 0 6.6 6.6l2.2-2.2a1 1 0 0 1 1-.25 11.4 11.4 0 0 0 3.6.57 1 1 0 0 1 1 1V20a1 1 0 0 1-1 1A17 17 0 0 1 3 4a1 1 0 0 1 1-1h3.5a1 1 0 0 1 1 1c0 1.25.2 2.45.57 3.57a1 1 0 0 1-.25 1z"/></svg><span>Phone:&nbsp; 1-800-555-0193</span></div>
  <div class="abs contact-row" style="left:718px;top:210px"><svg width="13" height="10" viewBox="0 0 24 18"><rect x="1" y="1" width="22" height="16" rx="2" fill="#555"/><path d="M2 2l10 8 10-8" stroke="#f4f4f4" stroke-width="2" fill="none"/></svg><span>info@brivon.ru</span></div>

  <h4 class="abs footer-heading" style="left:998px;top:64px">Quick links</h4>
  <ul class="abs quick-links" style="left:1002px;top:100px">
    <li>Home</li><li>Products</li><li>About us</li><li>Products</li><li>Velmar Academy</li><li>News</li><li>Contacts</li>
  </ul>
</footer>
<div class="abs copyright">&copy;2017 Brivon. All Rights Reserved.</div>

</body>
</html>
```